Neue Visitenkarten für internationales Beratungsunternehmen
Zielgruppe
Management Consulting, Management Beratung. Insgesamt beinhaltet das Portfolio wirklich Unternehmensberatung von der Vision zu Strategie, von der Strategie zu Businesss Architektur und Unternehmenszielen über Prozesse zu Prozessziele, Unternehmens(re)organisation bis hin zu IT Architektur und IT Beratung.
Prozessanalyse und Business Analyse sind wichtige Teile. IT Architektur beinhaltet all diese Aufgaben in der Software Beratung von der fachlichen Konzeption bis zur Implementierung bzw. Software Solution Design, Implementierung und Wartung, also das gesamte Software Life Cycle. Es handelt sich also um den Weg, wie man aus einer Vision ein IT-enabled Unternehmen aufzieht und zum Laufen bringt. Wir möchten Richtungsweisend sein in der Ausrichtung der Business Architektur, der Organisation, der Dienstleistungserbringung und der IT. Prozess-Überwachung (Reporting) und Prozess-Zertifizierung ist ein weitere Pfeiler. Wir bleiben immer am Puls des Unternehmens und am Puls seiner Prozesse. Das Ergebnis unserer Dienstleistung ist eine Lean IT enabled Solution und auch eine Lean Company. Da wir vieles anders machen ist unser Slogan 'We leave own tracks behind as we break new ground'. Es kann aber bald ein anderes folgen, wie 'Ihr Erfolg ist unser Ziel'.
Zur Zielgruppe gehören alle Mittelstands- und Großunternehmen, die ihr Business neu organisieren wollen, wie auch neu gegründete Unternehmen, die vom Anfang an ein Prozessorientiertes Vorgehen für Ihr Business anstreben. Diese Unternehmen können sowohl Dienstleistungen anbieten als auch aus dem produzierenden Gewerbe sein. Beispielhaft: aus After Sales oder sonstigen Services, Automotive, Versicherungen, Banken, Luftfahrt, Universitäten, Bildung, Chemie, Forschung, Medizin und Pharma und vieles mehr. Eine Einschränkung zur Zeit nicht angedacht. Neugründungen sind auf jeden Fall interessant. Es geht hauptsächlich um die Management Beratung und die Produktiv-Setzung solcher Firmen.
Aufgabenstellung
Das Projekt soll
1. ein Visitenkarte (fertig verwendbares und änderbares Template) und
2. ein entsprechend ansprechendes Briefpapier zum vordrucken für eine visionäre Firma finden und
3. soll das bisherige Logo und CI Farben einbinden und
4. nach Bedarf weitere passende Farben dazu finden.
Das Logo erhalten Sie hier von mir als RGB und CMYK *.pdf, und als *.psd, *.eps, *.ai auf Anforderung nachträglich zugesendet.
5. Das bevorzugte Logo ist das 2. oder 1. in der linken Spalte.
6. Die Unternehmensdaten für das Briefpapier finden Sie im angehängten Word-Dokument.
USt-Id und St-Nr werde noch vom FA vergeben. Diese zwei Werte sollten im Nachhinein noch anpassbar sein. Das wäre praktisch auch für alle anderen Texte (z.B. bei einem Firmenumzug).
7. Die Visitenkarte sollte folgende Angaben berücksichtigen:
Veltrano GmbH
www.veltrano-example.com
8. Ggf. Slogans wie die folgenden könnten verwendet werden:
The Harbor Weavers (ist bereits im Logo)
Lassen Sie Ihre Vision wahr werden
Veltrano® - Der Weg zum Erfolg
Business Process Solutions
9. Sollten Sie noch ein QR Code für gut finden oder eine sonstige Besonderheit, wie Klappkarten, so können wir das im Zuge des Projektes klären.
10. Hier kommen die CI Farben und Font Angaben: styleguide
Farben
* BLAUn (Azul)
CMYK - 76 - 19 0 86 in %
RGB - 14 - 42 - 65
RAL (Näherungswert) - Stahlblau 5011 ( Saphirblau 5003 , Schwarzblau 5004)
* Graun (Gris)
CMYK - 0 - 0 - 0 - 60 in %
RGB - 143 - 144 - 143
RAL (Näherungswert) - Verkehrsgrau 7042
Schriften (Fonts)
* Wortmarke (Logo) - Century Gothic Regular (Ableitung)
Diese Schrift sollte auch beim Firmennahmen bei der Adresse verwendet werden.
* Slogan - Open sans (google font)

```html
<!DOCTYPE html>
<html lang="de">
<head>
<meta charset="utf-8">
<title>Veltrano GmbH – Briefpapier und Kuvert</title>
<link rel="stylesheet" href="https://fonts.googleapis.com/css2?family=Open+Sans:wght@400;600;700&family=Questrial&display=swap">
<style>
  :root{
    --navy:#0e2a41;
    --grey:#8f908f;
    --paper:#ffffff;
    --ink:#1a1a1a;
    --muted:#6d6f72;
    --stage:#dcd9d5;
  }
  *{box-sizing:border-box;margin:0;padding:0}
  html,body{width:1200px;height:800px;overflow:hidden;background:var(--stage)}
  body{position:relative;font-family:"Open Sans",Arial,sans-serif;color:var(--ink)}
  .abs{position:absolute}

  /* Letterhead */
  .letter{left:43px;top:29px;width:521px;height:736px;background:var(--paper);box-shadow:0 2px 8px rgba(0,0,0,.25)}
  .letter-topbar{left:0;top:0;width:100%;height:8px;background:var(--grey)}
  .brand-name{font-family:"Questrial",sans-serif;color:var(--navy);letter-spacing:3px;white-space:nowrap}
  .letter .brand-name{left:61px;top:32px;font-size:30px}
  .brand-tagline{font-family:"Open Sans",sans-serif;color:var(--grey);letter-spacing:1.6px;white-space:nowrap}
  .letter .brand-tagline{left:106px;top:70px;font-size:9.5px}
  .sender{right:43px;text-align:right;font-size:7.6px;color:var(--muted);line-height:1;white-space:nowrap}
  .sender.company{top:32px;color:var(--navy);font-weight:600}
  .icon{left:484px;width:10px;height:10px}
  .window{left:48px;top:122px;width:178px;height:70px}
  .window .corner{width:9px;height:9px;border-color:var(--grey);border-style:solid;border-width:0}
  .return-line{left:13px;top:11px;font-size:4.6px;color:var(--muted);border-bottom:.6px solid var(--muted);padding-bottom:2px;white-space:nowrap;width:154px}
  .recipient{left:13px;top:29px;font-size:9.4px;line-height:12px}
  .ref{left:371px;width:124px;font-size:7.4px;display:flex;justify-content:space-between}
  .fold{left:0;width:19px;height:.6px;background:var(--grey)}
  .body-text{left:61px;font-size:8.6px;white-space:nowrap}
  .subject{font-weight:700;font-size:9px}
  .footer-name{left:62px;top:698px;width:84px;text-align:center;font-family:"Questrial",sans-serif;font-size:8px;color:var(--navy);font-weight:600}
  .footer-col{font-size:5.6px;color:var(--muted);line-height:7.6px;white-space:nowrap}
  .footer-col .label{color:var(--navy);font-size:6px}
  .footer-rule{top:677px;width:.6px;height:31px;background:var(--grey)}
  .line-navy{height:2px;background:var(--navy)}
  .band-grey{height:7px;background:var(--grey)}
  .url{display:flex;align-items:center;gap:4px;color:var(--navy);white-space:nowrap;font-family:"Open Sans",sans-serif}

  /* Envelope front */
  .envelope{left:629px;top:81px;width:542px;height:363px}
  .envelope-body{left:0;top:86px;width:542px;height:277px;background:var(--paper);box-shadow:0 2px 8px rgba(0,0,0,.25)}
  .envelope .brand-name{left:40px;top:112px;font-size:27px}
  .envelope .brand-tagline{left:82px;top:147px;font-size:8.6px}
  .envelope-sender{left:35px;top:162px;font-size:6.6px;color:var(--muted);white-space:nowrap}
  .envelope-sender b{color:var(--navy);font-weight:600}
  .env-window{left:32px;top:242px;width:218px;height:87px;border:1px solid #c9c9c9;border-radius:9px;background:linear-gradient(#f4f4f4,#ffffff 40%,#f7f7f7);box-shadow:inset 0 0 5px rgba(0,0,0,.12)}
  .env-address{left:43px;top:23px;font-family:Arial,sans-serif;font-size:6.8px;line-height:11.6px;color:#555}

  /* Envelope back */
  .envelope-back{left:632px;top:467px;width:543px;height:279px;background:var(--navy);box-shadow:0 2px 8px rgba(0,0,0,.3)}
  .flap-name{color:#8f9ba6;font-family:"Questrial",sans-serif;letter-spacing:2px;white-space:nowrap}
</style>
</head>
<body>

<!-- Letterhead -->
<section class="letter abs" aria-label="Briefpapier">
  <div class="letter-topbar abs"></div>

  <div class="brand-name abs">Veltrano®</div>
  <div class="brand-tagline abs">THE HARBOR WEAVERS</div>

  <div class="sender company abs">Veltrano GmbH</div>
  <div class="sender abs" style="top:42px;font-size:8px">Lindenweg 12b</div>
  <div class="sender abs" style="top:51px;font-size:8px">D-85000 Mustermoos</div>
  <div class="sender abs" style="top:66px;right:43px">+49 (0)8000-10 20 300</div>
  <div class="sender abs" style="top:83px">+49 (0)8000-10 20 381</div>
  <div class="sender abs" style="top:100px">+49 (0)170-00 12 34 56</div>
  <div class="sender abs" style="top:117px">H.Brankmann@veltrano-example.com</div>

  <svg class="icon abs" style="top:38px" viewBox="0 0 10 10" aria-hidden="true"><path d="M5 1 L10 5.5 H8.5 V9.5 H6 V7 H4 V9.5 H1.5 V5.5 H0 Z" fill="var(--navy)"/></svg>
  <svg class="icon abs" style="top:64px" viewBox="0 0 10 10" aria-hidden="true"><path d="M2.2 1 L4 2.8 L3 4.2 Q4.3 6 5.8 7 L7.2 6 L9 7.8 L7.6 9.2 Q3.5 8 0.8 2.4 Z" fill="var(--navy)"/></svg>
  <svg class="icon abs" style="top:81px" viewBox="0 0 10 10" aria-hidden="true"><rect x="2.5" y="1" width="5" height="3" fill="var(--navy)"/><rect x="0.5" y="4" width="9" height="4.5" rx="1" fill="var(--navy)"/><rect x="2.5" y="6.5" width="5" height="2.5" fill="#fff" stroke="var(--navy)" stroke-width=".6"/></svg>
  <svg class="icon abs" style="top:98px" viewBox="0 0 10 10" aria-hidden="true"><rect x="2" y="1.5" width="6" height="8" rx="1" transform="rotate(-35 5 5.5)" fill="none" stroke="var(--navy)" stroke-width="1.2"/></svg>
  <svg class="icon abs" style="top:115px" viewBox="0 0 10 10" aria-hidden="true"><rect x="0.5" y="2" width="9" height="6.5" fill="var(--navy)"/><path d="M0.8 2.4 L5 5.6 L9.2 2.4" fill="none" stroke="#fff" stroke-width=".8"/></svg>

  <div class="window abs">
    <div class="corner abs" style="left:0;top:0;border-left-width:.8px;border-top-width:.8px"></div>
    <div class="corner abs" style="right:0;top:0;border-right-width:.8px;border-top-width:.8px"></div>
    <div class="corner abs" style="left:0;bottom:0;border-left-width:.8px;border-bottom-width:.8px"></div>
    <div class="corner abs" style="right:0;bottom:0;border-right-width:.8px;border-bottom-width:.8px"></div>
    <div class="return-line abs">Veltrano GmbH · Lindenweg 12b · 85000 Mustermoos</div>
    <div class="recipient abs">Finanzamt Beispielstadt<br>z.Hd. Herrn …<br>85300 Beispielstadt</div>
  </div>

  <div class="ref abs" style="top:151px;font-weight:700"><span>Ihr Zeichen:</span><span>K05.1</span></div>
  <div class="ref abs" style="top:170px"><span>Seiten:</span><span>1</span></div>
  <div class="ref abs" style="top:188px"><span>Datum:</span><span>21.01.2015</span></div>

  <div class="fold abs" style="top:237px"></div>
  <div class="fold abs" style="top:484px"></div>

  <div class="body-text subject abs" style="top:250px">Steuerliche Erfassung für Veltrano GmbH</div>
  <div class="body-text abs" style="top:280px">Sehr geehrter Herr</div>
  <div class="body-text abs" style="top:311px">Mit freundlichen Grüßen</div>
  <div class="body-text abs" style="top:321px;left:135px;font-size:6px;color:var(--muted)">…</div>
  <div class="body-text abs" style="top:372px">Holger Brankmann</div>

  <div class="footer-name abs">Veltrano GmbH</div>
  <div class="footer-col abs" style="left:178px;top:674px"><div class="label">Bankverbindung:</div>Nordhafen Bank AG Essen<br>IBAN: DE00 1200 3400 5600 7800 90<br>BIC: NOHA DE 3E</div>
  <div class="footer-rule abs" style="left:302px"></div>
  <div class="footer-col abs" style="left:323px;top:679px"><div class="label">Steuernummer:</div>120/0000/0000<br>USt.- ID: DE 000000000</div>
  <div class="footer-rule abs" style="left:411px"></div>
  <div class="footer-col abs" style="left:437px;top:677px;font-size:6.6px;line-height:8px"><div class="label" style="font-size:6.8px">Filiale:</div>Talstraße 4<br>45500 Talheim</div>

  <div class="line-navy abs" style="left:0;top:711px;width:100%"></div>
  <div class="band-grey abs" style="left:0;top:718px;width:40px"></div>
  <div class="band-grey abs" style="left:165px;top:718px;width:356px"></div>
  <div class="url abs" style="left:44px;top:713px;font-size:11px">
    <svg width="11" height="11" viewBox="0 0 12 12" aria-hidden="true"><circle cx="6" cy="6" r="5.3" fill="none" stroke="var(--navy)" stroke-width="1"/><ellipse cx="6" cy="6" rx="2.4" ry="5.3" fill="none" stroke="var(--navy)" stroke-width=".8"/><path d="M0.8 6 H11.2 M1.6 3.4 H10.4 M1.6 8.6 H10.4" stroke="var(--navy)" stroke-width=".8"/></svg>
    <span>www.veltrano-example.com</span>
  </div>
</section>

<!-- Envelope front -->
<section class="envelope abs" aria-label="Kuvert Vorderseite">
  <svg class="abs" style="left:0;top:0" width="542" height="88" viewBox="0 0 542 88" aria-hidden="true">
    <path d="M0 88 L16 14 Q19 0 34 0 L508 0 Q523 0 526 14 L542 88 Z" fill="var(--navy)"/>
  </svg>
  <div class="flap-name abs" style="left:0;width:542px;top:30px;text-align:center;font-size:15px">Veltrano</div>

  <div class="envelope-body abs"></div>
  <div class="brand-name abs">Veltrano®</div>
  <div class="brand-tagline abs">THE HARBOR WEAVERS</div>
  <div class="envelope-sender abs"><b>Veltrano GmbH</b>&nbsp;&nbsp; Lindenweg 12b&nbsp; D-85000 Mustermoos</div>

  <div class="env-window abs">
    <div class="env-address abs">Marta Keller<br>Am Lerchenhang 7<br>53700 Sankt Beispiel<br>SCHWEIZ</div>
  </div>

  <div class="line-navy abs" style="left:0;top:342px;width:542px"></div>
  <div class="band-grey abs" style="left:0;top:349px;width:366px"></div>
  <div class="band-grey abs" style="left:498px;top:349px;width:44px"></div>
  <div class="url abs" style="left:370px;top:343px;font-size:12px">
    <svg width="12" height="12" viewBox="0 0 12 12" aria-hidden="true"><circle cx="6" cy="6" r="5.3" fill="none" stroke="var(--navy)" stroke-width="1"/><ellipse cx="6" cy="6" rx="2.4" ry="5.3" fill="none" stroke="var(--navy)" stroke-width=".8"/><path d="M0.8 6 H11.2 M1.6 3.4 H10.4 M1.6 8.6 H10.4" stroke="var(--navy)" stroke-width=".8"/></svg>
    <span style="font-size:10px">www.veltrano-example.com</span>
  </div>
</section>

<!-- Envelope back -->
<section class="envelope-back abs" aria-label="Kuvert Rückseite">
  <svg class="abs" style="left:0;top:0" width="543" height="90" viewBox="0 0 543 90" aria-hidden="true">
    <path d="M0 0 L24 76 Q28 86 40 86 L503 86 Q515 86 519 76 L543 0" fill="none" stroke="rgba(0,0,0,.28)" stroke-width="1.2"/>
  </svg>
  <div class="flap-name abs" style="left:0;width:543px;top:36px;text-align:center;font-size:15px">Veltrano</div>
</section>

</body>
</html>
```